Realtor branding business card

modern, simple and self branding. Broker office logo needs to be used but not emphasized. Looking to brand myself

Target Market(s)

buyers, sellers and investors

Industry/Entity Type

Realtor

Contact Information for Business Card

Sample of my current business card on file

Requirements
Must have
• my website - emilioverdaskt.com
• Realtor logo
• Fair housing logo
Nice to have
• Colors from office logo but not a must
Should not have
• Do not want headshot

```html
<!DOCTYPE html>
<html lang="en">
<head>
<meta charset="utf-8">
<title>Realtor Business Card</title>
<link href="https://fonts.googleapis.com/css2?family=Roboto:wght@400;500;700;900&display=swap" rel="stylesheet">
<style>
  :root {
    --navy: #25196e;
    --red: #d9251d;
    --white: #ffffff;
    --page: #ececec;
    --badge: #2b2b2b;
  }
  * { margin: 0; padding: 0; box-sizing: border-box; }
  html, body {
    width: 1125px; height: 1200px; overflow: hidden;
    background: var(--page);
    font-family: "Roboto", Arial, sans-serif;
  }
  .card {
    position: absolute;
    left: 171px;
    width: 826px;
    height: 471px;
    background: var(--white);
    overflow: hidden;
    box-shadow: 0 2px 6px rgba(0,0,0,0.25);
  }
  .card--front { top: 106px; }
  .card--back { top: 638px; height: 473px; }
  .card__shapes { position: absolute; inset: 0; width: 100%; height: 100%; }

  .agent {
    position: absolute; left: 50px; top: 188px;
    color: var(--white);
  }
  .agent__name { font-size: 27px; font-weight: 700; line-height: 1.1; }
  .agent__title { font-size: 19px; font-weight: 500; margin-top: 4px; }
  .agent__address { font-size: 18px; line-height: 25px; margin-top: 18px; }
  .agent__contacts { list-style: none; margin-top: 14px; font-size: 18px; }
  .agent__contacts li { display: flex; align-items: center; height: 26px; }
  .agent__contacts svg { width: 17px; height: 17px; margin-right: 10px; fill: var(--white); flex: none; }

  .brand { position: absolute; color: var(--navy); font-weight: 900; line-height: 0.95; }
  .brand__name { display: block; letter-spacing: -1px; }
  .brand__tag { display: block; letter-spacing: 1px; }
  .brand--front { right: 48px; top: 66px; text-align: right; }
  .brand--front .brand__name { font-size: 58px; }
  .brand--front .brand__tag { font-size: 34px; }
  .brand--back { left: 0; right: 0; top: 178px; text-align: center; }
  .brand--back .brand__name { font-size: 72px; }
  .brand--back .brand__tag { font-size: 40px; }

  .badges { position: absolute; right: 44px; bottom: 36px; display: flex; align-items: flex-end; gap: 6px; }
  .badge { background: var(--badge); }
  .badge--member { width: 34px; height: 44px; }
  .badge--housing { width: 58px; height: 58px; }
</style>
</head>
<body>
  <section class="card card--front">
    <svg class="card__shapes" viewBox="0 0 800 456" preserveAspectRatio="none" aria-hidden="true">
      <polygon points="0,0 104,0 0,127" fill="var(--navy)"/>
      <polygon points="183,0 569,456 0,456 0,217" fill="var(--red)"/>
    </svg>

    <div class="agent">
      <h1 class="agent__name">Emilio Verdask, PA</h1>
      <p class="agent__title">Realtor</p>
      <p class="agent__address">84 Lakeshore Crest Dr.<br>Cedar Harbor, FL 32990</p>
      <ul class="agent__contacts">
        <li><svg viewBox="0 0 24 24"><path d="M6.6 10.8a15.1 15.1 0 0 0 6.6 6.6l2.2-2.2c.3-.3.7-.4 1-.2 1.1.4 2.3.6 3.6.6.6 0 1 .4 1 1V20c0 .6-.4 1-1 1A17 17 0 0 1 3 4c0-.6.4-1 1-1h3.5c.6 0 1 .4 1 1 0 1.3.2 2.5.6 3.6.1.3 0 .7-.2 1z"/></svg>555.210.4400</li>
        <li><svg viewBox="0 0 24 24"><path d="M7 1h10a2 2 0 0 1 2 2v18a2 2 0 0 1-2 2H7a2 2 0 0 1-2-2V3a2 2 0 0 1 2-2zm0 3v14h10V4zm5 15.5a1 1 0 1 0 0 2 1 1 0 0 0 0-2z"/></svg>555.318.7720</li>
        <li><svg viewBox="0 0 24 24"><path d="M2 5h20v14H2zm2 2v.4l8 5 8-5V7zm0 2.8V17h16V9.8l-8 5z"/></svg>verdaskrealty@mailbox.com</li>
        <li><svg viewBox="0 0 24 24"><path d="M12 2a10 10 0 1 0 0 20 10 10 0 0 0 0-20zm-1 17.9A8 8 0 0 1 4.2 10.2L9 15v1a2 2 0 0 0 2 2zm6.9-2.5A2 2 0 0 0 16 16h-1v-3a1 1 0 0 0-1-1H8v-2h2a1 1 0 0 0 1-1V7h2a2 2 0 0 0 2-2v-.4a8 8 0 0 1 2.9 12.8z"/></svg>www.emilioverdaskt.com</li>
      </ul>
    </div>

    <div class="brand brand--front">
      <span class="brand__name">Keystone Nest</span>
      <span class="brand__tag">Realty Group</span>
    </div>

    <div class="badges">
      <div class="badge badge--member" role="img" aria-label="Realtor membership badge"></div>
      <div class="badge badge--housing" role="img" aria-label="Fair housing badge"></div>
    </div>
  </section>

  <section class="card card--back">
    <div class="brand brand--back">
      <span class="brand__name">Keystone Nest</span>
      <span class="brand__tag">Realty Group</span>
    </div>
  </section>
</body>
</html>
```